Creative Alcoholic Beverage Package Design Needed!

We need a packaging design for a new alcoholic beverage, including the brand name. Flavours will include Sangria and Margarita, and future line extensions as well. Package will be a box (see attached dieline and example of a competitive product) in a 3 liter format. The dimensions of the box need to match the dieline, but we can be creative on the printing of the box. The product inside will be of high-quality, so the design needs to match this
Updates

Need extra days to review

Target Market(s)

25 to 40 year old, 70% female, 30% male

Colors

Designer to choose colors to be used in the design.

Requirements
Must have
• Be attractive, colourful, modern
• clearly mention the flavour, and show the components of the flavour (Sangria : red wine and citrus) - Margarita (mexican inspiration, lime, etc.)
• Have a clear "brand name" along with the flavours
• Mention the quantity (3 liters), alcohol level : 10% alc./vol.

```html
<!DOCTYPE html>
<html lang="en">
<head>
<meta charset="utf-8">
<title>Vinaleza Sangria – 3 ltr Box</title>
<link rel="stylesheet" href="https://fonts.googleapis.com/css2?family=Cormorant+Garamond:wght@500;600&family=Crimson+Text:wght@400;600;700&display=swap">
<style>
  :root {
    --stage: #ececec;
    --carton-pink: #fbe7ee;
    --carton-pink-deep: #f6d9e3;
    --wine-red: #a8191e;
    --wine-dark: #6e0c12;
    --lime-green: #7fa653;
    --lime-pale: #e4e2b4;
    --ink: #1c1a1a;
    --muted: #8a6b72;
  }
  * { margin: 0; padding: 0; box-sizing: border-box; }
  html, body { width: 1200px; height: 1200px; overflow: hidden; }
  body { background: var(--stage); font-family: "Crimson Text", Georgia, serif; color: var(--ink); }

  .carton { position: absolute; top: 150px; left: 90px; display: flex; box-shadow: 0 20px 40px rgba(0,0,0,.12); }

  .panel { position: relative; height: 900px; background: var(--carton-pink); overflow: hidden; }
  .panel--front { width: 640px; }
  .panel--side { width: 380px; background: linear-gradient(180deg, var(--carton-pink), var(--carton-pink-deep)); border-left: 1px solid #ecc9d4; }

  .lime-slice { position: absolute; border-radius: 50%;
    background: radial-gradient(circle, #f4f1d2 0%, var(--lime-pale) 65%, #b9c98a 90%, var(--lime-green) 100%); }
  .lime-slice--top { width: 180px; height: 180px; top: -70px; left: -70px; }
  .lime-slice--bottom { width: 170px; height: 170px; bottom: 170px; right: -50px; }
  .lime-slice--side { width: 120px; height: 120px; top: 60px; right: -70px; }

  .brand-name { position: absolute; font-family: "Cormorant Garamond", Georgia, serif; font-weight: 600; color: var(--ink); white-space: nowrap; }
  .panel--front .brand-name { top: 110px; left: 150px; font-size: 112px; line-height: 1; }

  .flavour-banner { position: absolute; top: 330px; left: 0; width: 420px; height: 78px;
    background: var(--wine-red); clip-path: polygon(0 0, 90% 0, 100% 100%, 0 100%); }
  .flavour-banner__name { position: absolute; top: 2px; left: 50px; font-size: 66px; line-height: 78px;
    font-weight: 600; color: #fff; letter-spacing: 1px; white-space: nowrap; }
  .flavour-components { position: absolute; top: 412px; left: 72px; font-size: 34px; color: var(--wine-red); }

  .serve-photo { position: absolute; top: 470px; left: 30px; width: 520px; height: 410px; border-radius: 40% 30% 20% 50%;
    background: linear-gradient(135deg, #f8eef2 0%, #e9b8c3 40%, #b52530 75%, var(--wine-dark) 100%); }

  .volume { position: absolute; right: 30px; bottom: 40px; text-align: right; color: var(--ink); z-index: 2; }
  .volume__amount { font-size: 78px; font-weight: 700; line-height: .9; }
  .volume__amount span { font-size: 40px; font-weight: 600; }
  .volume__abv { font-size: 26px; }

  .panel--side .brand-name { top: 40px; left: 60px; font-size: 56px; line-height: 1; }
  .side-flavour { position: absolute; top: 110px; left: 120px; font-size: 28px; color: var(--wine-red); font-weight: 600; }
  .side-rule { position: absolute; left: 30px; right: 30px; height: 1px; background: var(--muted); }
  .side-rule--top { top: 160px; }
  .side-rule--bottom { top: 650px; }
  .side-intro { position: absolute; top: 175px; left: 30px; right: 30px; font-size: 18px; line-height: 1.35; font-weight: 600; }

  .components-band { position: absolute; top: 282px; left: 0; right: 0; height: 46px;
    background: linear-gradient(90deg, #fbe7ee 0%, #c9555b 45%, var(--wine-red) 100%);
    color: #fff; font-size: 24px; line-height: 46px; text-align: center; }

  .feature { position: absolute; left: 30px; right: 30px; display: flex; align-items: center; gap: 16px; }
  .feature--right { flex-direction: row-reverse; text-align: right; }
  .feature--serve { top: 350px; }
  .feature--tap { top: 450px; }
  .feature--citrus { top: 550px; }
  .feature__body { flex: 1; }
  .feature__icon { flex: 0 0 64px; width: 64px; height: 64px; border-radius: 50%; background: var(--lime-green);
    display: flex; align-items: center; justify-content: center; }
  .feature__title { font-size: 17px; font-weight: 700; color: var(--wine-red); }
  .feature__text { font-size: 14px; line-height: 1.3; }

  .tap-cutout { position: absolute; top: 690px; left: 80px; }
  .side-abv { position: absolute; bottom: 30px; right: 40px; font-size: 18px; color: #eebfcd; }
</style>
</head>
<body>
  <div class="carton">
    <section class="panel panel--front">
      <div class="lime-slice lime-slice--top" role="img" aria-label="Half lime slice in the corner"></div>
      <h1 class="brand-name">Vinaleza</h1>
      <div class="flavour-banner"><span class="flavour-banner__name">SANGRIA</span></div>
      <p class="flavour-components">Red Wine &amp; Citrus</p>
      <div class="serve-photo" role="img" aria-label="Red wine pouring into a tilted glass with lime slices"></div>
      <div class="lime-slice lime-slice--bottom" role="img" aria-label="Lime slice"></div>
      <div class="volume">
        <div class="volume__amount">3<span>ltr</span></div>
        <div class="volume__abv">10% alc.</div>
      </div>
    </section>

    <section class="panel panel--side">
      <div class="lime-slice lime-slice--side" role="img" aria-label="Lime slice at the edge"></div>
      <h2 class="brand-name">Vinaleza</h2>
      <p class="side-flavour">Sangria</p>
      <div class="side-rule side-rule--top"></div>
      <p class="side-intro">Crafted from ripe red grapes and fresh citrus, this sangria pours bright, fruity and smooth in every glass.</p>
      <div class="components-band">Red Wine &amp; Citrus</div>

      <div class="feature feature--serve">
        <div class="feature__body">
          <p class="feature__title">Serve chilled</p>
          <p class="feature__text">Pour over ice with sliced citrus for a bright finish.</p>
        </div>
        <div class="feature__icon">
          <svg width="34" height="34" viewBox="0 0 34 34" fill="none" stroke="#fff" stroke-width="2.2"><path d="M5 6h24L17 19z"/><path d="M17 19v10M11 29h12"/></svg>
        </div>
      </div>
      <div class="feature feature--tap feature--right">
        <div class="feature__body">
          <p class="feature__title">Easy tap</p>
          <p class="feature__text">Press the tap and pour; stays fresh for weeks.</p>
        </div>
        <div class="feature__icon">
          <svg width="34" height="34" viewBox="0 0 34 34" fill="none" stroke="#fff" stroke-width="2.2"><rect x="9" y="6" width="16" height="8" rx="2"/><path d="M14 14v8h6v-8M17 26v3"/></svg>
        </div>
      </div>
      <div class="feature feature--citrus">
        <div class="feature__body">
          <p class="feature__title">Real citrus</p>
          <p class="feature__text">Made with lemon and lime for a lively taste.</p>
        </div>
        <div class="feature__icon">
          <svg width="34" height="34" viewBox="0 0 34 34" fill="none" stroke="#fff" stroke-width="2.2"><circle cx="17" cy="17" r="12"/><circle cx="17" cy="17" r="8"/><path d="M17 9v16M9 17h16"/></svg>
        </div>
      </div>

      <div class="side-rule side-rule--bottom"></div>
      <svg class="tap-cutout" width="220" height="180" viewBox="0 0 220 180" fill="none" stroke="#444" stroke-width="2" stroke-dasharray="5 5">
        <path d="M2 20 L218 2 V110 Q190 110 190 140 V150 Q190 178 150 178 H90 Q50 178 50 150 V140 Q50 110 2 110 Z"/>
      </svg>
      <p class="side-abv">10% alc./vol.</p>
    </section>
  </div>
</body>
</html>
```